Retail Jewelry Business Card Design Project

We are in need of a new business card design for a retail jewelry store. This store is in the business of fine jewelry including but not specific to bridal jewelry, diamonds, designer jewelry and watches.

This store has been in business for 20 years but continues to strive for a modern professional appeal. The main colors use for this business are a royal blue, white and silver.

Target Market(s)

Target market is ages 18-50

Industry/Entity Type

Jewelry

Requirements
Must have
• Sales Person Name
Sales Person Email Address

Store Address
Store Phone
Website

Standard business card size. No odd shapes or sizes.
Nice to have
• Overall modern feel for card.

We have thought that a design with a nice feature of the logo on the back of the card would be nice but open to ideas.
Should not have
• No specific images of jewelry should be used.

```html
<!DOCTYPE html>
<html lang="en">
<head>
<meta charset="utf-8">
<title>Harlan Reed Fine Jewelry – Business Cards</title>
<link rel="stylesheet" href="https://fonts.googleapis.com/css2?family=Cinzel:wght@400&family=PT+Sans:wght@400&display=swap">
<style>
  :root {
    --page: #f2f2f4;
    --royal-deep: #1a1570;
    --royal: #2b2596;
    --royal-light: #4a44bf;
    --white: #ffffff;
    --silver: #d6d8e6;
  }
  * { margin: 0; padding: 0; box-sizing: border-box; }
  html, body { width: 1200px; height: 1024px; overflow: hidden; background: var(--page); }
  .canvas { position: relative; width: 1200px; height: 1024px; }

  .card {
    position: absolute;
    width: 700px;
    height: 400px;
    overflow: hidden;
    color: var(--white);
    box-shadow: 0 14px 30px rgba(20, 20, 60, 0.28);
  }
  .card-front { left: 70px; top: 80px; }
  .card-back  { left: 430px; top: 548px; }

  .card-pattern {
    position: absolute; inset: 0;
    background: radial-gradient(ellipse at 40% 35%, var(--royal-light) 0%, var(--royal) 45%, var(--royal-deep) 100%);
  }

  .brand {
    position: absolute;
    font-family: "Cinzel", serif;
    font-weight: 400;
    color: var(--white);
    text-align: center;
    line-height: 1.15;
  }
  .brand-name {
    display: block; font-size: 48px; letter-spacing: 1px;
    padding: 0 6px 4px; border-bottom: 2px solid var(--white);
  }
  .brand-line { display: block; font-size: 20px; letter-spacing: 6px; margin-top: 6px; }

  .card-front .brand { left: 50px; top: 40px; }
  .card-back .brand { left: 180px; top: 112px; }

  .person-name {
    position: absolute; left: 120px; top: 178px;
    font-family: "PT Sans", sans-serif; font-size: 26px; color: var(--white);
    display: flex; align-items: center; gap: 10px;
  }
  .person-name svg { width: 18px; height: 18px; }

  .contact {
    position: absolute;
    font-family: "PT Sans", sans-serif;
    font-size: 17px;
    line-height: 1.3;
    color: var(--silver);
  }
  .contact-item { display: flex; align-items: flex-start; gap: 10px; margin-bottom: 10px; }
  .contact-item svg { flex: none; width: 16px; height: 16px; margin-top: 3px; }

  .contact-reach { left: 120px; top: 250px; }
  .contact-store { left: 360px; top: 250px; width: 290px; }
  .contact-primary { left: 50px; top: 318px; }

  .back-web {
    position: absolute; left: 110px; top: 268px;
    font-family: "PT Sans", sans-serif; font-size: 17px; color: var(--silver);
  }
</style>
</head>
<body>
<main class="canvas">

  <section class="card card-front" aria-label="Business card, contact side">
    <div class="card-pattern" role="img" aria-label="Royal blue floral damask pattern background"></div>

    <div class="brand">
      <span class="brand-name">Harlan Reed</span>
      <span class="brand-line">FINE JEWELRY</span>
    </div>

    <p class="person-name">
      <svg viewBox="0 0 20 20" aria-hidden="true"><path d="M4 7l3-4h6l3 4-6 10z" fill="none" stroke="#fff" stroke-width="1.5"/><path d="M4 7h12" stroke="#fff" stroke-width="1.2"/></svg>
      Harlan Reed Whitmore
    </p>

    <div class="contact contact-reach">
      <p class="contact-item">
        <svg viewBox="0 0 16 16" aria-hidden="true"><rect x="2" y="3" width="12" height="10" rx="1.5" fill="none" stroke="#fff" stroke-width="1.4"/><circle cx="8" cy="11" r="0.9" fill="#fff"/></svg>
        000-000-000
      </p>
    </div>

    <div class="contact contact-store">
      <p class="contact-item">
        <svg viewBox="0 0 16 16" aria-hidden="true"><path d="M1 8l7-6 7 6h-2v6H9v-4H7v4H3V8z" fill="#fff"/></svg>
        <span>2210 Laurel Avenue Bayview City,<br>FL 32000</span>
      </p>
    </div>

    <div class="contact contact-primary">
      <p class="contact-item">
        <svg viewBox="0 0 16 16" aria-hidden="true"><rect x="1.5" y="3.5" width="13" height="9" fill="none" stroke="#fff" stroke-width="1.4"/><path d="M1.5 3.5l6.5 5 6.5-5" fill="none" stroke="#fff" stroke-width="1.4"/></svg>
        harlan@harlanreedjewelry.com
      </p>
      <p class="contact-item">
        <svg viewBox="0 0 16 16" aria-hidden="true"><circle cx="8" cy="8" r="6.3" fill="none" stroke="#fff" stroke-width="1.3"/><ellipse cx="8" cy="8" rx="2.6" ry="6.3" fill="none" stroke="#fff" stroke-width="1.1"/><path d="M1.8 8h12.4" stroke="#fff" stroke-width="1.1"/></svg>
        www.harlanreedjewelry.com
      </p>
    </div>
  </section>

  <section class="card card-back" aria-label="Business card, brand side">
    <div class="card-pattern" role="img" aria-label="Royal blue floral damask pattern background"></div>
    <div class="brand">
      <span class="brand-name">Harlan Reed</span>
      <span class="brand-line">FINE JEWELRY</span>
    </div>
    <p class="back-web">www.harlanreedjewelry.com</p>
  </section>

</main>
</body>
</html>
```